New IT Consulting Company needs new Branding

I need some business cards and logo created for new IT consulting company called Copperline Partners Pty Ltd.

We deal with enterprise IT solution and IT consulting Firm.
Assisting businesses with Technology Upgrades and System integration

We have no existing color schemes in mind but after something a little recognizable but elegant also.

We are looking for something that conveys a professional look.

Target Market(s)

Targeting small to medium businesses with 0-500 employees

Industry/Entity Type

Information Technology

Contact Information for Business Card

Name, Title , Mobile Contact, Phone Contact , Email and Website URL

Logo Text

CopperPartners Pty Ltd "Shaping Smart Systems with care"

Font styles to use
Serif
Sans Serif

Requirements
Nice to have
• Looking for one or two primary colors and sticking to geometric or symmetrical design for the logo

```html
<!DOCTYPE html>
<html lang="en">
<head>
<meta charset="utf-8">
<title>Copperline Partners Pty Ltd – Business Card</title>
<link rel="stylesheet" href="https://fonts.googleapis.com/css2?family=Source+Sans+3:wght@400;600;700&display=swap">
<style>
  :root {
    --stage-top: #2b2b2b;
    --stage-bottom: #040404;
    --card-white: #ffffff;
    --brand-blue: #2f7fcf;
    --name-blue: #1f5fb0;
    --text-dark: #2a2a2a;
    --back-top: #4b9ad8;
    --back-bottom: #0a56a8;
    --back-mark: rgba(10, 70, 150, 0.55);
  }
  * { margin: 0; padding: 0; box-sizing: border-box; }
  html, body { width: 1200px; height: 900px; overflow: hidden; }
  body {
    background: linear-gradient(180deg, var(--stage-top) 0%, #141414 55%, var(--stage-bottom) 100%);
    font-family: "Source Sans 3", "Myriad Pro", Arial, sans-serif;
    position: relative;
  }
  .card {
    position: absolute;
    top: 306px;
    width: 440px;
    height: 271px;
    border-radius: 10px;
    overflow: hidden;
  }
  .card-front { left: 149px; background: var(--card-white); }
  .card-back {
    left: 608px;
    background: linear-gradient(180deg, var(--back-top) 0%, var(--back-bottom) 100%);
  }

  /* front: brand block */
  .brand {
    position: absolute;
    left: 18px;
    width: 200px;
    top: 78px;
    text-align: center;
    color: var(--brand-blue);
    font-weight: 600;
  }
  .brand-dot {
    width: 24px; height: 24px;
    border-radius: 50%;
    background: var(--brand-blue);
    margin: 0 auto 22px;
  }
  .brand-name { font-size: 21px; letter-spacing: 0.5px; line-height: 1.15; }
  .brand-suffix { font-size: 15px; letter-spacing: 4px; margin-top: 2px; }

  /* front: contact block */
  .contact { position: absolute; left: 233px; top: 41px; color: var(--text-dark); }
  .person-name { font-size: 18.5px; font-weight: 700; color: var(--name-blue); line-height: 1.2; }
  .person-title { font-size: 12.5px; margin-top: 2px; }
  .address { font-size: 12.5px; line-height: 16px; margin-top: 17px; }
  .contact-list { list-style: none; margin-top: 11px; font-size: 12.5px; }
  .contact-list li { display: flex; align-items: center; height: 16px; }
  .contact-list svg { width: 9px; height: 9px; margin: 0 10px 0 4px; fill: var(--name-blue); }

  /* back */
  .back-name {
    position: absolute;
    inset: 0;
    display: flex;
    align-items: center;
    justify-content: center;
    color: var(--back-mark);
    font-weight: 600;
    font-size: 30px;
    letter-spacing: 1px;
  }
</style>
</head>
<body>
  <section class="card card-front" aria-label="Business card front">
    <div class="brand">
      <div class="brand-dot"></div>
      <div class="brand-name">Copperline Partners</div>
      <div class="brand-suffix">Pty Ltd</div>
    </div>
    <div class="contact">
      <div class="person-name">Marcus Hale</div>
      <div class="person-title">Managing Director</div>
      <div class="address">1234, Address Goes Here<br>Country Name, 123456</div>
      <ul class="contact-list">
        <li><svg viewBox="0 0 10 10" aria-hidden="true"><path d="M3 0h4a1 1 0 0 1 1 1v8a1 1 0 0 1-1 1H3a1 1 0 0 1-1-1V1a1 1 0 0 1 1-1zm0 1.5v6h4v-6z"/></svg>123-456-7890</li>
        <li><svg viewBox="0 0 10 10" aria-hidden="true"><path d="M0 4c0-2 2-3 5-3s5 1 5 3l-2 1-1-2H3L2 5zM2 6h6l1 3H1z"/></svg>123-456-7890</li>
        <li><svg viewBox="0 0 10 10" aria-hidden="true"><path d="M1 3h8v6H1zM3 0h4v3H3zM2 5h6v1H2z"/></svg>123-456-7890</li>
        <li><svg viewBox="0 0 10 10" aria-hidden="true"><path d="M0 2h10v6H0zM1 3l4 3 4-3z"/></svg>info@youremail.com</li>
        <li><svg viewBox="0 0 10 10" aria-hidden="true"><path d="M6 1l3 3-4 4-1-1 3-3-1-1-3 3 2 2-2 1-3-3z"/></svg>www.yourweb.com</li>
      </ul>
    </div>
  </section>

  <section class="card card-back" aria-label="Business card back">
    <div class="back-name">Copperline Partners</div>
  </section>
</body>
</html>
```